I want our new logo design to guide the colors and look of the home page. I want it to be vibrant and contemporary. We are a new religious education publishing company. I would like any colors used to describe the product below to be bright and cheerful, but also to look good with our logo colors
On our home page we are introducing a new product for second graders. The product name should look child friendly, but not silly. If there is a way to add reverence to the words FIRST RECONCILIATION and FIRST EUCHARIST, and still make it look like it is a product for children, that would be great.
The product will be called:
Wayfinder Gathering Set for the Welcoming Room
FIRST RECONCILIATION
FIRST EUCHARIST
THE PRODUCT DESCRIPTION SHOULD BE AS FOLLOWS
Field tested and designed for the special needs inclusive classroom
Kit includes high impact visuals, hands-on activities, manipulatives, games, and other teaching aids for total engagement of ALL students
Detailed catechist lesson plans to maximize learning and retention
Cost effective reusable kit
Bilingual
Somewhere it should say COMING SOON, because the product is not ready yet, but we are promoting it. I don't have a picture of this product yet, but above the product description, we need an empty box that we'll use when we're ready to upload the picture of the kit.
There should also be a statement near the product description that says: To learn more about the Wayfinder Set for the Welcoming Room, click here.
Web page links:
About Us
Products
Resources
Contact Us
I would also like a few links to be featured on the home page:
Lanterns Along the Young Road....learn more
"What Calls Us Home?"....learn more
Could It Be Something Else Entirely?...learn more
The Map and the Path...learn more
Open Table Storytelling
I have increased my budget and clarified my brief so that it's easier to understand. It's basically just a home page and a template for the other pages. There is no content on the other web pages that you have to work on. I just need a well designed home page and a nice template for the other pages.
Reason: I am extending the deadline for 2 days so that templates can be designed for 5 additional web pages. Please make each template a little different from the way you designed the home page. These pages can have blank picture boxes and dummy text to save you time. I am only interested in layout for the addtional pages. Thank you!
We've made a selection and wanted to thank all of you for your wonderful designs!

```html
<!DOCTYPE html>
<html lang="en">
<head>
<meta charset="utf-8">
<title>Contact Us – Harbor Light Catechetics</title>
<link rel="stylesheet" href="https://fonts.googleapis.com/css2?family=Open+Sans:wght@400;700&display=swap">
<style>
  :root {
    --header-brown: #432c18;
    --footer-brown: #261a0f;
    --nav-text: #3d2a14;
    --accent-red: #c8102e;
    --brand-text: #eadfca;
    --tagline: #c9b89c;
    --body-grey: #7a7a7a;
    --label-grey: #8a8a8a;
    --rule-grey: #b5b5b5;
    --field-blue: #84cde6;
    --button-top: #4dbcf2;
    --button-bottom: #1787d0;
    --footer-head: #8c7b62;
    --footer-text: #6e5d47;
    --footer-rule: #5a4a36;
    --social-one: #3b5b99;
    --social-two: #5fc4e8;
    --page: #ffffff;
  }
  * { box-sizing: border-box; margin: 0; padding: 0; }
  html, body { width: 1032px; height: 1200px; overflow: hidden; background: var(--page); }
  body { position: relative; font-family: "Open Sans", Verdana, sans-serif; color: var(--body-grey); }

  .site-header {
    position: absolute; left: 0; top: 0; width: 1032px; height: 168px;
    background: var(--header-brown);
    box-shadow: 0 3px 6px rgba(0,0,0,0.35);
  }
  .brand-name {
    position: absolute; left: 0; width: 1032px; top: 98px; text-align: center;
    font-family: "Open Sans", Verdana, sans-serif; font-weight: 400;
    font-size: 26px; line-height: 30px; color: var(--brand-text);
  }
  .brand-tagline {
    position: absolute; left: 406px; width: 260px; top: 133px; text-align: right;
    font-family: "Open Sans", Verdana, sans-serif; font-size: 15px; line-height: 17px;
    color: var(--tagline);
  }

  .main-nav a {
    position: absolute; top: 196px; font-size: 19px; line-height: 22px;
    color: var(--nav-text); text-decoration: none; letter-spacing: 0.2px;
  }
  .main-nav .is-current { border-bottom: 1.5px solid var(--accent-red); padding-bottom: 3px; }

  .our-details { position: absolute; left: 121px; top: 290px; width: 230px; }
  .section-title { font-size: 17px; font-weight: 700; color: var(--label-grey); letter-spacing: 0.3px; line-height: 20px; }
  .our-details p { font-size: 13.5px; line-height: 16px; letter-spacing: 0.4px; margin-top: 14px; color: var(--body-grey); }
  .our-details p + p { margin-top: 16px; }
  .details-rule { position: absolute; left: 362px; top: 292px; height: 156px; border-left: 1px dotted var(--rule-grey); }

  .message-form { position: absolute; left: 437px; top: 290px; }
  .message-form .section-title { position: absolute; left: 0; top: 0; white-space: nowrap; }
  .field-label { position: absolute; left: 0; font-size: 14px; line-height: 16px; letter-spacing: 0.5px; color: var(--label-grey); white-space: nowrap; }
  .field-box { position: absolute; left: 0; height: 29px; border: 1px solid var(--field-blue); background: #fff; }
  .field-box.is-long { width: 304px; }
  .field-box.is-short { width: 224px; }
  .field-box.is-message { width: 436px; height: 221px; }
  .send-button {
    position: absolute; left: 0; top: 638px; width: 89px; height: 31px;
    border-radius: 4px; background: linear-gradient(var(--button-top), var(--button-bottom));
    color: #fff; font-size: 16px; font-weight: 700; text-align: center; line-height: 31px;
  }

  .site-footer { position: absolute; left: 0; top: 1033px; width: 1032px; height: 167px; background: var(--footer-brown); }
  .footer-col { position: absolute; top: 0; }
  .footer-head { position: absolute; top: 22px; font-size: 20px; font-weight: 700; letter-spacing: 0.6px; color: var(--footer-head); white-space: nowrap; line-height: 24px; }
  .footer-text { position: absolute; font-size: 13.5px; line-height: 20px; letter-spacing: 0.4px; color: var(--footer-text); white-space: nowrap; }
  .footer-rule { position: absolute; top: 26px; height: 125px; border-left: 1px dotted var(--footer-rule); }
  .social-tile { position: absolute; top: 57px; width: 29px; height: 29px; border-radius: 3px; }
  .social-tile.is-first { background: var(--social-one); }
  .social-tile.is-second { background: var(--social-two); }
</style>
</head>
<body>
  <header class="site-header">
    <div class="brand-name">Harbor Light Catechetics</div>
    <div class="brand-tagline">a new approach to catechesis</div>
  </header>

  <nav class="main-nav">
    <a href="#" style="left:187px">HOME</a>
    <a href="#" style="left:272px">ABOUT US</a>
    <a href="#" style="left:400px">PRODUCTS</a>
    <a href="#" style="left:542px">RESOURCES</a>
    <a href="#" class="is-current" style="left:696px">CONTACT US</a>
  </nav>

  <section class="our-details">
    <h2 class="section-title">Our details:</h2>
    <p>Harbor Light Catechetics<br>14 Elm Lane<br>Riverton NSW 2100</p>
    <p>T: +61 555.010.442<br>F: +61 555.010.443</p>
    <p>E: hello@harborlightcat.com</p>
  </section>
  <div class="details-rule"></div>

  <section class="message-form">
    <h2 class="section-title">Or send us a message:</h2>
    <span class="field-label" style="top:53px">Name:</span>
    <div class="field-box is-long" style="top:75px"></div>
    <span class="field-label" style="top:132px">E-mail:</span>
    <div class="field-box is-long" style="top:153px"></div>
    <span class="field-label" style="top:211px">Phone:</span>
    <div class="field-box is-short" style="top:232px"></div>
    <span class="field-label" style="top:290px">Subject:</span>
    <div class="field-box is-long" style="top:313px"></div>
    <span class="field-label" style="top:369px">Message:</span>
    <div class="field-box is-message" style="top:392px"></div>
    <div class="send-button">Send</div>
  </section>

  <footer class="site-footer">
    <div class="footer-col" style="left:62px">
      <h3 class="footer-head">CONTACT</h3>
      <p class="footer-text" style="top:53px">14 Elm Lane<br>Riverton NSW 2100<br>555.010.442<br>hello@harborlightcat.com</p>
    </div>
    <div class="footer-rule" style="left:305px"></div>
    <div class="footer-col" style="left:333px">
      <h3 class="footer-head">HARBOR LIGHT CATECHETICS</h3>
      <p class="footer-text" style="top:53px">HOME &nbsp;| &nbsp;ABOUT US &nbsp;| &nbsp;PRODUCTS &nbsp;| &nbsp;RESOURCES &nbsp;| CONTACT US</p>
      <p class="footer-text" style="top:77px">PRIVACY &nbsp;| &nbsp;SITE MAP</p>
      <p class="footer-text" style="top:112px">© 2011 Harbor Light Catechetics</p>
    </div>
    <div class="footer-rule" style="left:833px"></div>
    <div class="footer-col" style="left:861px">
      <h3 class="footer-head">FIND US</h3>
      <span class="social-tile is-first" style="left:1px" role="img" aria-label="Social network link"></span>
      <span class="social-tile is-second" style="left:44px" role="img" aria-label="Social network link"></span>
    </div>
  </footer>
</body>
</html>
```